Fern Hollow Animal Hospital Postcard Design

I need a postcard for grand opening. The front of the card should have our business name and logo, below the logo I want to have a coupon for " Free office visit or $ 20 off of packages " for the first time clients.

I want to have the packages prices and details on the back of the postcard, the details of the packages are attached.

```html
<!DOCTYPE html>
<html lang="en">
<head>
<meta charset="utf-8">
<title>Fern Hollow Animal Hospital – Grand Opening Postcard</title>
<link rel="stylesheet" href="https://fonts.googleapis.com/css2?family=Arimo:wght@400;700&family=Cormorant+Garamond:wght@500&family=Pinyon+Script&display=swap">
<style>
  :root {
    --green: #155a3b;
    --sand: #f1dbc5;
    --sand-light: #f7e8d8;
    --white: #ffffff;
  }
  * { margin: 0; padding: 0; box-sizing: border-box; }
  html, body { width: 1200px; height: 602px; overflow: hidden; background: var(--white); }
  .postcard {
    position: relative;
    width: 1200px;
    height: 602px;
    background: var(--sand);
    overflow: hidden;
    font-family: "Arimo", Arial, sans-serif;
  }
  .brand-block {
    position: absolute;
    left: 90px; top: 0;
    width: 220px; height: 118px;
    background: var(--green);
    display: flex; align-items: center; justify-content: center;
  }
  .brand-name {
    font-family: "Cormorant Garamond", Georgia, serif;
    font-weight: 500;
    font-size: 38px;
    color: var(--sand-light);
    line-height: 1;
  }
  .headline {
    position: absolute;
    left: 0; top: 0;
    font-family: "Pinyon Script", cursive;
    font-weight: 400;
    color: var(--green);
    line-height: 1;
  }
  .headline span { position: absolute; white-space: nowrap; font-size: 98px; }
  .headline .line-one { left: 92px; top: 165px; }
  .headline .line-two { left: 178px; top: 255px; }
  .coupon {
    position: absolute;
    left: 90px; top: 380px;
    width: 363px; height: 141px;
    background: var(--white);
    border: 2px solid var(--green);
    border-radius: 12px;
    overflow: hidden;
    color: var(--green);
    text-align: center;
  }
  .coupon-offer { padding-top: 18px; }
  .coupon-offer p { font-size: 25px; line-height: 1.3; }
  .coupon-offer .amount { font-size: 28px; }
  .coupon-offer strong { font-weight: 700; }
  .coupon-terms {
    position: absolute;
    left: 0; bottom: 0;
    width: 100%; height: 38px;
    background: var(--green);
    color: var(--white);
    font-size: 18px;
    line-height: 38px;
  }
  .feature-art { position: absolute; left: 0; top: 0; }
  .footer-strip {
    position: absolute;
    left: 0; top: 540px;
    width: 1200px; height: 12px;
    background: var(--sand-light);
  }
  .footer-bar {
    position: absolute;
    left: 0; bottom: 0;
    width: 1200px; height: 50px;
    background: var(--green);
    color: var(--white);
    font-size: 20px;
    display: flex; align-items: center; justify-content: space-between;
    padding: 0 54px 0 68px;
  }
  .footer-bar strong { font-weight: 700; }
</style>
</head>
<body>
<main class="postcard">
  <svg class="feature-art" width="1200" height="602" viewBox="0 0 1200 602">
    <defs>
      <clipPath id="above-footer"><rect x="0" y="0" width="1200" height="540"/></clipPath>
      <linearGradient id="pet-photo-tone" x1="0" y1="0" x2="1" y2="1">
        <stop offset="0" stop-color="#ffffff"/>
        <stop offset="0.55" stop-color="#f6ecdd"/>
        <stop offset="1" stop-color="#e9e4df"/>
      </linearGradient>
    </defs>
    <g clip-path="url(#above-footer)">
      <circle cx="1139" cy="330" r="514" fill="var(--green)"/>
      <circle cx="1139" cy="330" r="496" fill="var(--sand-light)"/>
      <circle cx="1139" cy="330" r="489" fill="url(#pet-photo-tone)" role="img" aria-label="Photo of a cream puppy hugging a sleeping grey kitten"/>
    </g>
  </svg>

  <div class="brand-block"><span class="brand-name">Fern Hollow</span></div>

  <h1 class="headline"><span class="line-one">Grand</span><span class="line-two">Opening</span></h1>

  <section class="coupon">
    <div class="coupon-offer">
      <p>Free office visit or</p>
      <p class="amount"><strong>$20 off</strong> of packages</p>
    </div>
    <p class="coupon-terms">for the first time clients.</p>
  </section>

  <div class="footer-strip"></div>
  <footer class="footer-bar">
    <span>Visit us: <strong>fernhollowvet@mailbox.net</strong></span>
    <span>Contact us: <strong>555-310-0427</strong></span>
  </footer>
</main>
</body>
</html>
```